Demo Screens Needed for Recruiting with AI App

We are in the process of raising money for our startup called KelvoraLink. We need demos to show investors what we're trying to do with images. We really love the simplicity and modern look of the Pivlo App and want something similar. We will have the "swipe" functionality similar to Flarvi as well. The sample images I've attached are only for caregivers but long term this will be for all industries. There will also be a rewards page for loyalty membership. The current landing page is www.kelvoralink-demo.com. That will show you the color scheme and logo.

```html
<!DOCTYPE html>
<html lang="en">
<head>
<meta charset="utf-8">
<title>KelvoraLink – App Screens</title>
<link rel="stylesheet" href="https://fonts.googleapis.com/css2?family=Poppins:wght@400;500;600;700&display=swap">
<style>
  :root{
    --brand:#0f6e96;
    --brand-deep:#0b5474;
    --brand-soft:#e6f2f8;
    --ink:#1d2733;
    --muted:#7c8794;
    --line:#e7ecf0;
    --canvas:#f3f6f8;
    --card:#ffffff;
    --star:#f4b400;
    --ok:#2fb36b;
    --heart:#e0313c;
    --dot-green:#b7dc6a;
    --dot-yellow:#f6d36b;
  }
  *{box-sizing:border-box;margin:0;padding:0}
  html,body{width:1200px;height:3124px;overflow:hidden}
  body{background:var(--canvas);font-family:"Poppins",sans-serif;color:var(--ink)}
  .showcase{display:flex;flex-direction:column}
  .screen-row{height:781px;display:flex;justify-content:center;align-items:center;gap:45px}
  .screen{width:330px;height:714px;background:var(--card);border-radius:38px;position:relative;overflow:hidden;box-shadow:0 18px 40px rgba(15,60,90,.12);display:flex;flex-direction:column}
  .status-bar{height:44px;padding:14px 26px 0;display:flex;justify-content:space-between;font-size:13px;font-weight:600}
  .status-bar svg{width:54px;height:12px}

  /* onboarding */
  .onboard{padding-bottom:28px}
  .brand-name{margin:40px 0 0 30px;font-size:26px;letter-spacing:5px;font-weight:500;color:var(--brand)}
  .intro-card{margin:34px 22px 0;position:relative;height:250px}
  .msg{display:flex;align-items:center;gap:10px}
  .msg-in{position:absolute;top:0;left:0}
  .msg-out{position:absolute;bottom:0;right:0}
  .avatar{width:48px;height:48px;border-radius:50%;background:linear-gradient(135deg,#c9a58d,#5b4a45);flex:none}
  .avatar.small{width:40px;height:40px}
  .bubble{background:var(--card);box-shadow:0 4px 14px rgba(0,0,0,.08);border-radius:14px;font-size:10px;padding:8px 12px;color:var(--muted);max-width:130px;line-height:1.4}
  .headline{position:absolute;top:86px;left:10px;right:10px;font-size:19px;line-height:1.3;font-weight:700;color:var(--ink)}
  .accent-dot{position:absolute;border-radius:50%}
  .dot-a{width:14px;height:14px;background:var(--dot-green);left:40px;top:390px}
  .dot-b{width:10px;height:10px;background:var(--dot-yellow);right:60px;top:420px}
  .dot-c{width:8px;height:8px;background:var(--brand-soft);left:150px;top:455px}
  .onboard-actions{margin-top:auto;padding:0 26px;text-align:center}
  .btn-primary{display:block;background:var(--brand);color:#fff;border-radius:12px;padding:14px;font-size:13px;font-weight:600;letter-spacing:1px;text-decoration:none}
  .text-link{display:block;margin-top:16px;font-size:12px;font-weight:600;color:var(--brand);letter-spacing:1px;text-decoration:none}
  .legal{margin-top:18px;font-size:9.5px;color:var(--muted);line-height:1.5}
  .legal span{color:var(--brand);text-decoration:underline}

  /* list */
  .list{background:#f7fafc}
  .list-head{display:flex;justify-content:space-between;align-items:center;padding:14px 20px 10px}
  .list-head h2{font-size:22px;font-weight:600}
  .icon-btn{width:30px;height:30px;border-radius:50%;background:var(--card);box-shadow:0 2px 8px rgba(0,0,0,.08);display:flex;align-items:center;justify-content:center}
  .filter-pill{margin:0 20px 12px;background:var(--card);border:1px solid var(--line);border-radius:10px;font-size:9.5px;color:var(--muted);padding:9px 12px;display:flex;justify-content:space-between;letter-spacing:.5px}
  .profile-card{margin:0 14px 12px;background:var(--card);border-radius:16px;padding:14px;box-shadow:0 4px 14px rgba(0,0,0,.05)}
  .card-top{display:flex;gap:10px;align-items:center}
  .card-name{font-size:13px;font-weight:600}
  .card-loc{font-size:9.5px;color:var(--muted)}
  .card-desc{font-size:9.5px;color:var(--muted);line-height:1.5;margin:10px 0}
  .card-tags{display:flex;gap:6px;align-items:center}
  .tag{font-size:9px;border:1px solid var(--line);border-radius:20px;padding:3px 9px;color:var(--ink)}
  .tag-fill{margin-left:auto;background:var(--brand);color:#fff;font-size:9px;border-radius:6px;padding:4px 10px}
  .card-meta{display:flex;justify-content:space-between;align-items:center;margin-top:10px}
  .stars{color:var(--star);font-size:13px;letter-spacing:1px}
  .price{font-size:11px;font-weight:600}
  .view-link{display:block;text-align:center;margin-top:10px;font-size:10px;font-weight:600;color:var(--brand);letter-spacing:1px}
  .tab-bar{margin-top:auto;height:62px;border-top:1px solid var(--line);background:var(--card);display:flex;justify-content:space-around;align-items:center;padding-bottom:8px}
  .tab-bar svg{width:20px;height:20px}

  /* profile */
  .profile-photo{height:330px;background:linear-gradient(160deg,#dfe9e4 0%,#9fb9b2 45%,#3c3a3f 100%)}
  .profile-body{margin-top:-22px;background:var(--card);border-radius:22px 22px 0 0;padding:18px 20px 0;position:relative}
  .profile-title{display:flex;justify-content:space-between;align-items:center}
  .profile-title h3{font-size:15px;font-weight:600}
  .status-pill{font-size:9px;color:var(--ok);display:flex;align-items:center;gap:4px}
  .status-pill::before{content:"";width:6px;height:6px;border-radius:50%;background:var(--ok)}
  .trait-grid{display:grid;grid-template-columns:1fr 1fr;gap:8px;margin-top:12px}
  .trait{border:1px solid var(--line);border-radius:12px;padding:10px;text-align:center;font-size:10px;color:var(--muted)}
  .trait svg{display:block;margin:0 auto 4px;width:18px;height:18px}
</style>
</head>
<body>
<main class="showcase">

  <!-- row 1 -->
  <div class="screen-row">
    <section class="screen onboard">
      <div class="status-bar"><span>9:41</span><svg viewBox="0 0 54 12"><rect x="0" y="6" width="3" height="6" fill="#1d2733"/><rect x="5" y="4" width="3" height="8" fill="#1d2733"/><rect x="10" y="2" width="3" height="10" fill="#1d2733"/><rect x="30" y="1" width="22" height="10" rx="3" fill="none" stroke="#1d2733"/><rect x="32" y="3" width="16" height="6" rx="1" fill="#1d2733"/></svg></div>
      <div class="brand-name">KELVORALINK</div>
      <div class="intro-card">
        <div class="msg msg-in"><div class="avatar" role="img" aria-label="Caregiver portrait photo"></div><p class="bubble">Thank you for being here, growing together</p></div>
        <h1 class="headline">Unlocking the Power of Meaningful Connections</h1>
        <div class="msg msg-out"><p class="bubble">Awesome!</p><div class="avatar small" role="img" aria-label="Family member portrait photo"></div></div>
      </div>
      <span class="accent-dot dot-a"></span><span class="accent-dot dot-b"></span><span class="accent-dot dot-c"></span>
      <div class="onboard-actions">
        <a class="btn-primary">GET STARTED</a>
        <a class="text-link">LOG IN</a>
        <p class="legal">By clicking get started you are agreeing to our <span>privacy policy</span> and <span>terms &amp; agreements</span>.</p>
      </div>
    </section>

    <section class="screen list">
      <div class="status-bar"><span>9:41</span><svg viewBox="0 0 54 12"><rect x="0" y="6" width="3" height="6" fill="#1d2733"/><rect x="5" y="4" width="3" height="8" fill="#1d2733"/><rect x="10" y="2" width="3" height="10" fill="#1d2733"/><rect x="30" y="1" width="22" height="10" rx="3" fill="none" stroke="#1d2733"/><rect x="32" y="3" width="16" height="6" rx="1" fill="#1d2733"/></svg></div>
      <div class="list-head"><h2>Find your tribe</h2><span class="icon-btn"><svg width="14" height="14" viewBox="0 0 14 14"><circle cx="6" cy="6" r="4.5" fill="none" stroke="#0f6e96" stroke-width="1.6"/><line x1="9.5" y1="9.5" x2="13" y2="13" stroke="#0f6e96" stroke-width="1.6"/></svg></span></div>
      <div class="filter-pill"><span>YES JOBS · YES BOOKING BIDS</span><span>⌄</span></div>
      <article class="profile-card">
        <div class="card-top"><div class="avatar small" role="img" aria-label="Caregiver portrait photo"></div><div><p class="card-name">Elena Varo Quist</p><p class="card-loc">Yuba, CA</p></div></div>
        <p class="card-desc">Caring companion with years of experience in senior and family home support.</p>
        <div class="card-tags"><span class="tag">CNA</span><span class="tag">5 yrs exp</span><span class="tag-fill">Hire</span></div>
        <div class="card-meta"><span class="stars">★★★★★</span><span class="price">From $22/hr</span></div>
        <span class="view-link">VIEW PROFILE</span>
      </article>
      <article class="profile-card">
        <div class="card-top"><div class="avatar small" role="img" aria-label="Caregiver portrait photo"></div><div><p class="card-name">Tomas Reyl Danner</p><p class="card-loc">Yuba, CA</p></div></div>
        <p class="card-desc">Patient helper for daily routines, meals and mobility assistance.</p>
        <div class="card-tags"><span class="tag">HHA</span><span class="tag">3 yrs exp</span><span class="tag-fill">Hire</span></div>
        <div class="card-meta"><span class="stars">★★★★☆</span><span class="price">From $20/hr</span></div>
      </article>
      <nav class="tab-bar"><svg viewBox="0 0 20 20"><path d="M3 9l7-6 7 6v8H3z" fill="#0f6e96"/></svg><svg viewBox="0 0 20 20"><path d="M3 4h14v10H8l-4 3z" fill="none" stroke="#7c8794" stroke-width="1.6"/></svg><svg viewBox="0 0 20 20"><path d="M10 17s-7-4.5-7-9a3.6 3.6 0 017-1.3A3.6 3.6 0 0117 8c0 4.5-7 9-7 9z" fill="none" stroke="#7c8794" stroke-width="1.6"/></svg></nav>
    </section>

    <section class="screen profile">
      <div class="profile-photo" role="img" aria-label="Caregiver portrait photo"></div>
      <div class="profile-body">
        <div class="profile-title"><h3>Elena Varo Quist</h3><span class="status-pill">Available</span></div>
        <p class="card-loc">Yuba, CA</p>
        <p class="card-desc">Caring companion with years of experience in senior and family home support.</p>
        <div class="card-meta"><span class="stars">★★★★★</span><span class="price">From $22/hr</span></div>
        <div class="trait-grid">
          <div class="trait"><svg viewBox="0 0 18 18"><circle cx="9" cy="7" r="4" fill="none" stroke="#0f6e96" stroke-width="1.5"/><line x1="9" y1="11" x2="9" y2="17" stroke="#0f6e96" stroke-width="1.5"/></svg>Female</div>
          <div class="trait"><svg viewBox="0 0 18 18"><path d="M9 15s-6-3.8-6-7.6A3 3 0 019 6a3 3 0 016 1.4C15 11.2 9 15 9 15z" fill="none" stroke="#0f6e96" stroke-width="1.5"/></svg>Single</div>
        </div>
      </div>
      <nav class="tab-bar"><svg viewBox="0 0 20 20"><path d="M3 9l7-6 7 6v8H3z" fill="none" stroke="#7c8794" stroke-width="1.6"/></svg><svg viewBox="0 0 20 20"><path d="M3 4h14v10H8l-4 3z" fill="none" stroke="#7c8794" stroke-width="1.6"/></svg><svg viewBox="0 0 20 20"><path d="M10 17s-7-4.5-7-9a3.6 3.6 0 017-1.3A3.6 3.6 0 0117 8c0 4.5-7 9-7 9z" fill="#e0313c"/></svg></nav>
    </section>
  </div>

  <!-- row 2 -->
  <div class="screen-row">
    <section class="screen onboard">
      <div class="status-bar"><span>9:41</span><svg viewBox="0 0 54 12"><rect x="0" y="6" width="3" height="6" fill="#1d2733"/><rect x="5" y="4" width="3" height="8" fill="#1d2733"/><rect x="10" y="2" width="3" height="10" fill="#1d2733"/><rect x="30" y="1" width="22" height="10" rx="3" fill="none" stroke="#1d2733"/><rect x="32" y="3" width="16" height="6" rx="1" fill="#1d2733"/></svg></div>
      <div class="brand-name">KELVORALINK</div>
      <div class="intro-card">
        <div class="msg msg-in"><div class="avatar" role="img" aria-label="Caregiver portrait photo"></div><p class="bubble">Thank you for being here, growing together</p></div>
        <h1 class="headline">Unlocking the Power of Meaningful Connections</h1>
        <div class="msg msg-out"><p class="bubble">Awesome!</p><div class="avatar small" role="img" aria-label="Family member portrait photo"></div></div>
      </div>
      <span class="accent-dot dot-a"></span><span class="accent-dot dot-b"></span><span class="accent-dot dot-c"></span>
      <div class="onboard-actions">
        <a class="btn-primary">GET STARTED</a>
        <a class="text-link">LOG IN</a>
        <p class="legal">By clicking get started you are agreeing to our <span>privacy policy</span> and <span>terms &amp; agreements</span>.</p>
      </div>
    </section>

    <section class="screen list">
      <div class="status-bar"><span>9:41</span><svg viewBox="0 0 54 12"><rect x="0" y="6" width="3" height="6" fill="#1d2733"/><rect x="5" y="4" width="3" height="8" fill="#1d2733"/><rect x="10" y="2" width="3" height="10" fill="#1d2733"/><rect x="30" y="1" width="22" height="10" rx="3" fill="none" stroke="#1d2733"/><rect x="32" y="3" width="16" height="6" rx="1" fill="#1d2733"/></svg></div>
      <div class="list-head"><h2>Find your tribe</h2><span class="icon-btn"><svg width="14" height="14" viewBox="0 0 14 14"><circle cx="6" cy="6" r="4.5" fill="none" stroke="#0f6e96" stroke-width="1.6"/><line x1="9.5" y1="9.5" x2="13" y2="13" stroke="#0f6e96" stroke-width="1.6"/></svg></span></div>
      <div class="filter-pill"><span>YES JOBS · YES BOOKING BIDS</span><span>⌄</span></div>
      <article class="profile-card">
        <div class="card-top"><div class="avatar small" role="img" aria-label="Caregiver portrait photo"></div><div><p class="card-name">Elena Varo Quist</p><p class="card-loc">Yuba, CA</p></div></div>
        <p class="card-desc">Caring companion with years of experience in senior and family home support.</p>
        <div class="card-tags"><span class="tag">CNA</span><span class="tag">5 yrs exp</span><span class="tag-fill">Hire</span></div>
        <div class="card-meta"><span class="stars">★★★★★</span><span class="price">From $22/hr</span></div>
        <span class="view-link">VIEW PROFILE</span>
      </article>
      <article class="profile-card">
        <div class="card-top"><div class="avatar small" role="img" aria-label="Caregiver portrait photo"></div><div><p class="card-name">Tomas Reyl Danner</p><p class="card-loc">Yuba, CA</p></div></div>
        <p class="card-desc">Patient helper for daily routines, meals and mobility assistance.</p>
        <div class="card-tags"><span class="tag">HHA</span><span class="tag">3 yrs exp</span><span class="tag-fill">Hire</span></div>
        <div class="card-meta"><span class="stars">★★★★☆</span><span class="price">From $20/hr</span></div>
      </article>
      <nav class="tab-bar"><svg viewBox="0 0 20 20"><path d="M3 9l7-6 7 6v8H3z" fill="#0f6e96"/></svg><svg viewBox="0 0 20 20"><path d="M3 4h14v10H8l-4 3z" fill="none" stroke="#7c8794" stroke-width="1.6"/></svg><svg viewBox="0 0 20 20"><path d="M10 17s-7-4.5-7-9a3.6 3.6 0 017-1.3A3.6 3.6 0 0117 8c0 4.5-7 9-7 9z" fill="none" stroke="#7c8794" stroke-width="1.6"/></svg></nav>
    </section>

    <section class="screen profile">
      <div class="profile-photo" role="img" aria-label="Caregiver portrait photo"></div>
      <div class="profile-body">
        <div class="profile-title"><h3>Elena Varo Quist</h3><span class="status-pill">Available</span></div>
        <p class="card-loc">Yuba, CA</p>
        <p class="card-desc">Caring companion with years of experience in senior and family home support.</p>
        <div class="card-meta"><span class="stars">★★★★★</span><span class="price">From $22/hr</span></div>
        <div class="trait-grid">
          <div class="trait"><svg viewBox="0 0 18 18"><circle cx="9" cy="7" r="4" fill="none" stroke="#0f6e96" stroke-width="1.5"/><line x1="9" y1="11" x2="9" y2="17" stroke="#0f6e96" stroke-width="1.5"/></svg>Female</div>
          <div class="trait"><svg viewBox="0 0 18 18"><path d="M9 15s-6-3.8-6-7.6A3 3 0 019 6a3 3 0 016 1.4C15 11.2 9 15 9 15z" fill="none" stroke="#0f6e96" stroke-width="1.5"/></svg>Single</div>
        </div>
      </div>
      <nav class="tab-bar"><svg viewBox="0 0 20 20"><path d="M3 9l7-6 7 6v8H3z" fill="none" stroke="#7c8794" stroke-width="1.6"/></svg><svg viewBox="0 0 20 20"><path d="M3 4h14v10H8l-4 3z" fill="none" stroke="#7c8794" stroke-width="1.6"/></svg><svg viewBox="0 0 20 20"><path d="M10 17s-7-4.5-7-9a3.6 3.6 0 017-1.3A3.6 3.6 0 0117 8c0 4.5-7 9-7 9z" fill="#e0313c"/></svg></nav>
    </section>
  </div>

  <!-- row 3 -->
  <div class="screen-row">
    <section class="screen onboard">
      <div class="status-bar"><span>9:41</span><svg viewBox="0 0 54 12"><rect x="0" y="6" width="3" height="6" fill="#1d2733"/><rect x="5" y="4" width="3" height="8" fill="#1d2733"/><rect x="10" y="2" width="3" height="10" fill="#1d2733"/><rect x="30" y="1" width="22" height="10" rx="3" fill="none" stroke="#1d2733"/><rect x="32" y="3" width="16" height="6" rx="1" fill="#1d2733"/></svg></div>
      <div class="brand-name">KELVORALINK</div>
      <div class="intro-card">
        <div class="msg msg-in"><div class="avatar" role="img" aria-label="Caregiver portrait photo"></div><p class="bubble">Thank you for being here, growing together</p></div>
        <h1 class="headline">Unlocking the Power of Meaningful Connections</h1>
        <div class="msg msg-out"><p class="bubble">Awesome!</p><div class="avatar small" role="img" aria-label="Family member portrait photo"></div></div>
      </div>
      <span class="accent-dot dot-a"></span><span class="accent-dot dot-b"></span><span class="accent-dot dot-c"></span>
      <div class="onboard-actions">
        <a class="btn-primary">GET STARTED</a>
        <a class="text-link">LOG IN</a>
        <p class="legal">By clicking get started you are agreeing to our <span>privacy policy</span> and <span>terms &amp; agreements</span>.</p>
      </div>
    </section>

    <section class="screen profile">
      <div class="profile-photo" role="img" aria-label="Caregiver portrait photo"></div>
      <div class="profile-body">
        <div class="profile-title"><h3>Elena Varo Quist</h3><span class="status-pill">Available</span></div>
        <p class="card-loc">Yuba, CA</p>
        <p class="card-desc">Caring companion with years of experience in senior and family home support.</p>
        <div class="card-meta"><span class="stars">★★★★★</span><span class="price">From $22/hr</span></div>
        <div class="trait-grid">
          <div class="trait"><svg viewBox="0 0 18 18"><circle cx="9" cy="7" r="4" fill="none" stroke="#0f6e96" stroke-width="1.5"/><line x1="9" y1="11" x2="9" y2="17" stroke="#0f6e96" stroke-width="1.5"/></svg>Female</div>
          <div class="trait"><svg viewBox="0 0 18 18"><path d="M9 15s-6-3.8-6-7.6A3 3 0 019 6a3 3 0 016 1.4C15 11.2 9 15 9 15z" fill="none" stroke="#0f6e96" stroke-width="1.5"/></svg>Single</div>
        </div>
      </div>
      <nav class="tab-bar"><svg viewBox="0 0 20 20"><path d="M3 9l7-6 7 6v8H3z" fill="none" stroke="#7c8794" stroke-width="1.6"/></svg><svg viewBox="0 0 20 20"><path d="M3 4h14v10H8l-4 3z" fill="none" stroke="#7c8794" stroke-width="1.6"/></svg><svg viewBox="0 0 20 20"><path d="M10 17s-7-4.5-7-9a3.6 3.6 0 017-1.3A3.6 3.6 0 0117 8c0 4.5-7 9-7 9z" fill="#e0313c"/></svg></nav>
    </section>

    <section class="screen list">
      <div class="status-bar"><span>9:41</span><svg viewBox="0 0 54 12"><rect x="0" y="6" width="3" height="6" fill="#1d2733"/><rect x="5" y="4" width="3" height="8" fill="#1d2733"/><rect x="10" y="2" width="3" height="10" fill="#1d2733"/><rect x="30" y="1" width="22" height="10" rx="3" fill="none" stroke="#1d2733"/><rect x="32" y="3" width="16" height="6" rx="1" fill="#1d2733"/></svg></div>
      <div class="list-head"><h2>Find your tribe</h2><span class="icon-btn"><svg width="14" height="14" viewBox="0 0 14 14"><circle cx="6" cy="6" r="4.5" fill="none" stroke="#0f6e96" stroke-width="1.6"/><line x1="9.5" y1="9.5" x2="13" y2="13" stroke="#0f6e96" stroke-width="1.6"/></svg></span></div>
      <div class="filter-pill"><span>YES JOBS · YES BOOKING BIDS</span><span>⌄</span></div>
      <article class="profile-card">
        <div class="card-top"><div class="avatar small" role="img" aria-label="Caregiver portrait photo"></div><div><p class="card-name">Elena Varo Quist</p><p class="card-loc">Yuba, CA</p></div></div>
        <p class="card-desc">Caring companion with years of experience in senior and family home support.</p>
        <div class="card-tags"><span class="tag">CNA</span><span class="tag">5 yrs exp</span><span class="tag-fill">Hire</span></div>
        <div class="card-meta"><span class="stars">★★★★★</span><span class="price">From $22/hr</span></div>
        <span class="view-link">VIEW PROFILE</span>
      </article>
      <article class="profile-card">
        <div class="card-top"><div class="avatar small" role="img" aria-label="Caregiver portrait photo"></div><div><p class="card-name">Tomas Reyl Danner</p><p class="card-loc">Yuba, CA</p></div></div>
        <p class="card-desc">Patient helper for daily routines, meals and mobility assistance.</p>
        <div class="card-tags"><span class="tag">HHA</span><span class="tag">3 yrs exp</span><span class="tag-fill">Hire</span></div>
        <div class="card-meta"><span class="stars">★★★★☆</span><span class="price">From $20/hr</span></div>
      </article>
      <nav class="tab-bar"><svg viewBox="0 0 20 20"><path d="M3 9l7-6 7 6v8H3z" fill="#0f6e96"/></svg><svg viewBox="0 0 20 20"><path d="M3 4h14v10H8l-4 3z" fill="none" stroke="#7c8794" stroke-width="1.6"/></svg><svg viewBox="0 0 20 20"><path d="M10 17s-7-4.5-7-9a3.6 3.6 0 017-1.3A3.6 3.6 0 0117 8c0 4.5-7 9-7 9z" fill="none" stroke="#7c8794" stroke-width="1.6"/></svg></nav>
    </section>
  </div>

  <!-- row 4 -->
  <div class="screen-row">
    <section class="screen onboard">
      <div class="status-bar"><span>9:41</span><svg viewBox="0 0 54 12"><rect x="0" y="6" width="3" height="6" fill="#1d2733"/><rect x="5" y="4" width="3" height="8" fill="#1d2733"/><rect x="10" y="2" width="3" height="10" fill="#1d2733"/><rect x="30" y="1" width="22" height="10" rx="3" fill="none" stroke="#1d2733"/><rect x="32" y="3" width="16" height="6" rx="1" fill="#1d2733"/></svg></div>
      <div class="brand-name">KELVORALINK</div>
      <div class="intro-card">
        <div class="msg msg-in"><div class="avatar" role="img" aria-label="Caregiver portrait photo"></div><p class="bubble">Thank you for being here, growing together</p></div>
        <h1 class="headline">Unlocking the Power of Meaningful Connections</h1>
        <div class="msg msg-out"><p class="bubble">Awesome!</p><div class="avatar small" role="img" aria-label="Family member portrait photo"></div></div>
      </div>
      <span class="accent-dot dot-a"></span><span class="accent-dot dot-b"></span><span class="accent-dot dot-c"></span>
      <div class="onboard-actions">
        <a class="btn-primary">GET STARTED</a>
        <a class="text-link">LOG IN</a>
        <p class="legal">By clicking get started you are agreeing to our <span>privacy policy</span> and <span>terms &amp; agreements</span>.</p>
      </div>
    </section>

    <section class="screen profile">
      <div class="profile-photo" role="img" aria-label="Caregiver portrait photo"></div>
      <div class="profile-body">
        <div class="profile-title"><h3>Elena Varo Quist</h3><span class="status-pill">Available</span></div>
        <p class="card-loc">Yuba, CA</p>
        <p class="card-desc">Caring companion with years of experience in senior and family home support.</p>
        <div class="card-meta"><span class="stars">★★★★★</span><span class="price">From $22/hr</span></div>
        <div class="trait-grid">
          <div class="trait"><svg viewBox="0 0 18 18"><circle cx="9" cy="7" r="4" fill="none" stroke="#0f6e96" stroke-width="1.5"/><line x1="9" y1="11" x2="9" y2="17" stroke="#0f6e96" stroke-width="1.5"/></svg>Female</div>
          <div class="trait"><svg viewBox="0 0 18 18"><path d="M9 15s-6-3.8-6-7.6A3 3 0 019 6a3 3 0 016 1.4C15 11.2 9 15 9 15z" fill="none" stroke="#0f6e96" stroke-width="1.5"/></svg>Single</div>
        </div>
      </div>
      <nav class="tab-bar"><svg viewBox="0 0 20 20"><path d="M3 9l7-6 7 6v8H3z" fill="none" stroke="#7c8794" stroke-width="1.6"/></svg><svg viewBox="0 0 20 20"><path d="M3 4h14v10H8l-4 3z" fill="none" stroke="#7c8794" stroke-width="1.6"/></svg><svg viewBox="0 0 20 20"><path d="M10 17s-7-4.5-7-9a3.6 3.6 0 017-1.3A3.6 3.6 0 0117 8c0 4.5-7 9-7 9z" fill="#e0313c"/></svg></nav>
    </section>

    <section class="screen list">
      <div class="status-bar"><span>9:41</span><svg viewBox="0 0 54 12"><rect x="0" y="6" width="3" height="6" fill="#1d2733"/><rect x="5" y="4" width="3" height="8" fill="#1d2733"/><rect x="10" y="2" width="3" height="10" fill="#1d2733"/><rect x="30" y="1" width="22" height="10" rx="3" fill="none" stroke="#1d2733"/><rect x="32" y="3" width="16" height="6" rx="1" fill="#1d2733"/></svg></div>
      <div class="list-head"><h2>Find your tribe</h2><span class="icon-btn"><svg width="14" height="14" viewBox="0 0 14 14"><circle cx="6" cy="6" r="4.5" fill="none" stroke="#0f6e96" stroke-width="1.6"/><line x1="9.5" y1="9.5" x2="13" y2="13" stroke="#0f6e96" stroke-width="1.6"/></svg></span></div>
      <div class="filter-pill"><span>YES JOBS · YES BOOKING BIDS</span><span>⌄</span></div>
      <article class="profile-card">
        <div class="card-top"><div class="avatar small" role="img" aria-label="Caregiver portrait photo"></div><div><p class="card-name">Elena Varo Quist</p><p class="card-loc">Yuba, CA</p></div></div>
        <p class="card-desc">Caring companion with years of experience in senior and family home support.</p>
        <div class="card-tags"><span class="tag">CNA</span><span class="tag">5 yrs exp</span><span class="tag-fill">Hire</span></div>
        <div class="card-meta"><span class="stars">★★★★★</span><span class="price">From $22/hr</span></div>
        <span class="view-link">VIEW PROFILE</span>
      </article>
      <article class="profile-card">
        <div class="card-top"><div class="avatar small" role="img" aria-label="Caregiver portrait photo"></div><div><p class="card-name">Tomas Reyl Danner</p><p class="card-loc">Yuba, CA</p></div></div>
        <p class="card-desc">Patient helper for daily routines, meals and mobility assistance.</p>
        <div class="card-tags"><span class="tag">HHA</span><span class="tag">3 yrs exp</span><span class="tag-fill">Hire</span></div>
        <div class="card-meta"><span class="stars">★★★★☆</span><span class="price">From $20/hr</span></div>
      </article>
      <nav class="tab-bar"><svg viewBox="0 0 20 20"><path d="M3 9l7-6 7 6v8H3z" fill="#0f6e96"/></svg><svg viewBox="0 0 20 20"><path d="M3 4h14v10H8l-4 3z" fill="none" stroke="#7c8794" stroke-width="1.6"/></svg><svg viewBox="0 0 20 20"><path d="M10 17s-7-4.5-7-9a3.6 3.6 0 017-1.3A3.6 3.6 0 0117 8c0 4.5-7 9-7 9z" fill="none" stroke="#7c8794" stroke-width="1.6"/></svg></nav>
    </section>
  </div>

</main>
</body>
</html>
```